Increasing performance of Security Operations Centers

Halvorent builds Security Operations Centers (SOC) that enable Meridian 500 clients to be proactive and predictive in the way they secure their people and facilities. The methods involve automating threat detection, streamlining workflows, and outsourcing the most appropriate tasks. The outcomes are a reduction in total incidents and faster response times with fewer resources so clients can focus on their core business.
We're looking for 2 slides to replace the attached PPT. The first slide would be broken into each of the 8 capabilities when presenting: i.e. starting with "Reduce incidents..." on the first slide, building on with "Better direct..." on the second and continuing around clockwise. I'm looking for a more compelling way to present the capabilities and am not wedded to the way it is laid out now.
Also attached is our brand book for color and font values to comply with.

I will extend the deadline to 3/28 as soon as I figure out how.

```html
<!DOCTYPE html>
<html lang="en">
<head>
<meta charset="utf-8">
<title>SOC Performance Improvement Objectives – Halvorent</title>
<link href="https://fonts.googleapis.com/css2?family=Arimo:wght@400;700&display=swap" rel="stylesheet">
<style>
  :root {
    --navy: #0b3f63;
    --red: #c0302b;
    --white: #ffffff;
    --backdrop: #bdbdbf;
    --rule: #ececec;
  }
  * { box-sizing: border-box; margin: 0; padding: 0; }
  html, body { width: 960px; height: 1200px; overflow: hidden; background: var(--backdrop); }
  body { font-family: "Arimo", Arial, sans-serif; }
  .board {
    position: absolute; left: 0; top: 0;
    width: 1200px; height: 1500px;
    transform: scale(0.8); transform-origin: 0 0;
  }
  .slide {
    position: absolute; left: 157px;
    width: 886px; height: 665px;
    background: var(--white); overflow: hidden;
  }
  .slide--objectives { top: 91px; }
  .slide--summary { top: 786px; }
  .slide__header {
    position: absolute; left: 0; top: 0; width: 100%; height: 112px;
    background: var(--navy); border-bottom: 8px solid var(--red);
  }
  .slide__footer {
    position: absolute; left: 0; bottom: 0; width: 100%; height: 78px;
    background: var(--navy); border-top: 8px solid var(--red);
  }
  .slide__title {
    position: absolute; left: 43px; top: 40px;
    color: var(--white); font-weight: 400; font-size: 35px; letter-spacing: 0.2px;
    white-space: nowrap;
  }
  .slide__brand {
    position: absolute; right: 52px; bottom: 16px;
    color: var(--white); font-size: 35px; font-weight: 400; letter-spacing: 0.3px;
  }
  .divider {
    position: absolute; left: 0; right: 0; top: 315px; height: 1px; background: var(--rule);
  }
  .pill {
    position: absolute; width: 294px; height: 72px; border-radius: 36px;
    display: flex; align-items: center; padding: 0 20px 0 26px;
    color: var(--white); font-size: 15.5px; line-height: 19px;
  }
  .pill--red { background: var(--red); }
  .pill--navy { background: var(--navy); }
  .pill--left { left: 43px; }
  .pill--right { left: 549px; }
  .hub {
    position: absolute; left: 335px; top: 250px; width: 216px; height: 216px;
    border-radius: 50%; background: var(--navy);
    display: flex; align-items: center; justify-content: center; text-align: center;
    color: var(--white); font-weight: 700; font-size: 27px; line-height: 32px;
  }
  .headline {
    position: absolute; left: 0; right: 0; top: 160px; text-align: center;
    color: var(--navy); font-weight: 700; font-size: 28px; line-height: 35px;
  }
  .headline em { font-style: normal; color: var(--red); }
  .tagline {
    position: absolute; left: 0; right: 0; top: 524px; text-align: center;
    color: var(--navy); font-weight: 700; font-size: 28px;
  }
</style>
</head>
<body>
<main class="board">

  <section class="slide slide--objectives">
    <div class="slide__header"></div>
    <h1 class="slide__title">SOC Performance Improvement Objectives…</h1>
    <div class="divider"></div>

    <div class="pill pill--red pill--left" style="top:166px">Reduce&nbsp; incidents, respond faster,<br>with fewer resources</div>
    <div class="pill pill--navy pill--left" style="top:270px">Reduce Total Cost</div>
    <div class="pill pill--red pill--left" style="top:374px">Outsource Key or Non-Core<br>Functions</div>
    <div class="pill pill--navy pill--left" style="top:479px">Automate threat detection,<br>streamline workflows,</div>

    <div class="pill pill--red pill--right" style="top:166px">Increase your installed systems<br>protective usefulness &amp; adaptability<br>to new threats</div>
    <div class="pill pill--navy pill--right" style="top:270px">Lessen your management burden.</div>
    <div class="pill pill--red pill--right" style="top:374px">Better direct your security/safety<br>personnel to situations where they<br>are needed most.</div>
    <div class="pill pill--navy pill--right" style="top:479px">Free up time for more engagement,<br>deterrence, and investigations.</div>

    <div class="hub"></div>
    <div class="slide__footer"></div>
    <div class="slide__brand">halvorent</div>
  </section>

  <section class="slide slide--summary">
    <div class="slide__header"></div>
    <h1 class="slide__title">SOC Performance Improvement Objectives…</h1>
    <div class="divider"></div>

    <p class="headline">Reduce&nbsp; <em>Incidents</em>, Respond <em>Faster</em><br>with Fewer <em>Resources</em></p>
    <div class="hub">Reduce Total<br>Cost of<br>Operations</div>
    <p class="tagline">Proactive, Predictive and Preventative</p>

    <div class="slide__footer"></div>
    <div class="slide__brand">halvorent</div>
  </section>

</main>
</body>
</html>
```